Flyer-Design für Immobilienmakler und Hausverwaltung
Zielgruppe
Wir sind Immobilienmakler und Hausverwaltung und suchen Eigentümer, die Ihre Immobilie veräußern wollen bzw. verwalten lassen möchten.
valtmer-immobilien.example Farbwahl in Himmelblau zu dunkelflieder Bitte.
Der Flyer soll für den Bereich Makler sein.
Aufgabenstellung
Der Flyer sollte in Din A5 sein. Bitte noch einen Rabatt von 20 % auf die Maklerprovision einarbeiten und ein kostenloses Vorgespräch.

```html
<!DOCTYPE html>
<html lang="de">
<head>
<meta charset="utf-8">
<title>Valtmer Immobilien – Flyer</title>
<link rel="stylesheet" href="https://fonts.googleapis.com/css2?family=Arimo:ital,wght@0,400;0,700;1,400;1,700&family=Kaushan+Script&family=Great+Vibes&display=swap">
<style>
  :root {
    --sky: #4398d8;
    --lilac: #7a0078;
    --navy: #0b4a6f;
    --paper: #f1f1f2;
    --white: #ffffff;
  }
  * { margin: 0; padding: 0; box-sizing: border-box; }
  html, body { width: 852px; height: 1200px; overflow: hidden; background: var(--paper); }
  .flyer {
    position: relative; width: 852px; height: 1200px; overflow: hidden;
    background: var(--paper); font-family: "Arimo", Arial, sans-serif;
  }
  .hero-photo {
    position: absolute; left: 0; top: 0; width: 852px; height: 600px;
    background:
      radial-gradient(ellipse at 45% 30%, #5f8f5a 0%, #7aa86a 22%, transparent 48%),
      radial-gradient(ellipse at 50% 70%, #e3b6a0 0%, #d9a08c 30%, transparent 60%),
      linear-gradient(180deg, #ece8e3 0%, #e6dcd4 60%, #d8cfc8 100%);
  }
  .shapes { position: absolute; left: 0; top: 0; width: 852px; height: 1200px; }
  .discount-badge {
    position: absolute; left: 60px; top: 0; width: 154px; height: 163px;
    background: var(--sky); border-radius: 0 0 77px 77px;
    color: var(--white); text-align: center; font-weight: 700;
    padding-top: 8px;
  }
  .discount-badge .percent { font-size: 48px; line-height: 46px; letter-spacing: -1px; }
  .discount-badge .word { font-size: 37px; line-height: 36px; letter-spacing: -1px; }
  .discount-badge .note { font-size: 14px; line-height: 13px; margin-top: 4px; letter-spacing: -0.3px; }
  .brand-mark {
    position: absolute; right: 24px; top: 28px;
    font-weight: 700; font-size: 20px; color: var(--navy); letter-spacing: 1px;
  }
  .free-talk {
    position: absolute; left: 490px; top: 272px;
    font-family: "Kaushan Script", cursive; font-size: 36px; color: var(--white);
    transform: rotate(-9deg); transform-origin: left bottom; white-space: nowrap;
    text-shadow: 0 1px 3px rgba(0,0,0,0.25);
  }
  .company-name {
    position: absolute; left: 12px; top: 324px;
    font-weight: 700; font-size: 58px; letter-spacing: 1px; color: var(--navy);
    white-space: nowrap;
    text-shadow: 2px 0 0 #fff, -2px 0 0 #fff, 0 2px 0 #fff, 0 -2px 0 #fff;
  }
  .company-tagline {
    position: absolute; left: 96px; top: 378px; width: 501px; height: 33px;
    background: var(--sky); border-radius: 6px;
    color: var(--white); font-style: italic; font-weight: 700; font-size: 18px;
    letter-spacing: 4.6px; line-height: 33px; padding-left: 8px; white-space: nowrap;
  }
  .service-title {
    position: absolute; left: 30px; top: 704px; width: 330px; text-align: center;
    color: var(--navy); font-weight: 700; font-size: 34px; line-height: 37px; letter-spacing: 7px;
  }
  .service-list { position: absolute; left: 30px; top: 806px; list-style: none; }
  .service-list li {
    display: flex; align-items: center; height: 33.6px;
    color: var(--navy); font-style: italic; font-size: 21px; letter-spacing: 5.5px;
  }
  .service-list svg { width: 30px; height: 22px; margin-right: 17px; }
  .pitch-title {
    position: absolute; left: 404px; top: 598px;
    color: var(--sky); font-weight: 700; font-size: 37px; line-height: 40.5px; letter-spacing: 2.5px;
  }
  .pitch-text {
    position: absolute; left: 406px; top: 774px; width: 430px;
    color: var(--navy); font-size: 13px; line-height: 16px; letter-spacing: 1px;
  }
  .benefits { position: absolute; left: 416px; top: 886px; list-style: none; }
  .benefits li { display: flex; align-items: center; height: 42px; }
  .benefits .dot { width: 32px; height: 32px; border-radius: 50%; background: var(--navy); margin-right: 20px; flex: none; }
  .benefits p { color: var(--navy); font-size: 10px; line-height: 13px; letter-spacing: 0.8px; width: 270px; }
  .benefits li.strong p { font-weight: 700; }
  .slogan {
    position: absolute; left: 0; top: 1112px; width: 852px; text-align: center;
    font-family: "Great Vibes", cursive; font-size: 45px; line-height: 50px; color: var(--white); white-space: nowrap;
  }
  .contact-row {
    position: absolute; left: 6px; top: 1168px; width: 840px; height: 28px;
    display: flex; align-items: center; justify-content: space-between; color: var(--white);
    font-weight: 700; font-size: 15px; letter-spacing: 2px; white-space: nowrap;
  }
  .contact-row .item { display: flex; align-items: center; }
  .contact-row .icon {
    width: 26px; height: 26px; border-radius: 50%; background: var(--white);
    display: flex; align-items: center; justify-content: center; margin-right: 8px;
  }
  .contact-row .icon svg { width: 16px; height: 16px; }
</style>
</head>
<body>
<main class="flyer">
  <div class="hero-photo" role="img" aria-label="Foto: zwei Hände halten ein kleines Einfamilienhaus mit Garten, Bäumen, Auto und Hund"></div>

  <svg class="shapes" viewBox="0 0 852 1200" aria-hidden="true">
    <path fill="var(--sky)" d="M0,514 C70,590 150,606 230,592 C320,576 400,490 493,453 L852,453 L852,1200 L0,1200 Z"/>
    <path fill="var(--lilac)" d="M404,536 C480,480 560,451 640,451 C730,451 800,495 852,540 L852,1200 L404,1200 Z"/>
    <path fill="var(--paper)" d="M0,605 C70,645 130,655 190,648 C280,636 350,580 404,536 C500,495 580,486 650,490 C740,498 810,560 852,630 L852,1200 L0,1200 Z"/>
    <path fill="var(--sky)" d="M540,1108 C680,1092 790,1040 852,985 L852,1200 L540,1200 Z"/>
    <path fill="var(--lilac)" d="M0,1085 C180,1060 380,1090 560,1108 C690,1110 790,1070 852,1040 L852,1200 L0,1200 Z"/>
  </svg>

  <div class="discount-badge">
    <div class="percent">20%</div>
    <div class="word">Rabatt</div>
    <div class="note">auf die<br>Maklerprovision</div>
  </div>

  <div class="brand-mark">Valtmer</div>

  <div class="free-talk">Kostenloses Vorgespräch</div>

  <div class="company-tagline">Hausverwaltung&amp;Immobilienmakler</div>
  <h1 class="company-name">Valtmer Immobilien</h1>

  <h2 class="service-title">Unser Service für Sie...</h2>
  <ul class="service-list">
    <li><svg viewBox="0 0 30 22"><path d="M3,11 L11,19 L27,3" fill="none" stroke="var(--sky)" stroke-width="5" stroke-linecap="round" stroke-linejoin="round"/></svg>Lorem ipsum dolor</li>
    <li><svg viewBox="0 0 30 22"><path d="M3,11 L11,19 L27,3" fill="none" stroke="var(--sky)" stroke-width="5" stroke-linecap="round" stroke-linejoin="round"/></svg>Lorem ipsum dolor</li>
    <li><svg viewBox="0 0 30 22"><path d="M3,11 L11,19 L27,3" fill="none" stroke="var(--sky)" stroke-width="5" stroke-linecap="round" stroke-linejoin="round"/></svg>Lorem ipsum dolor</li>
    <li><svg viewBox="0 0 30 22"><path d="M3,11 L11,19 L27,3" fill="none" stroke="var(--sky)" stroke-width="5" stroke-linecap="round" stroke-linejoin="round"/></svg>Lorem ipsum dolor</li>
    <li><svg viewBox="0 0 30 22"><path d="M3,11 L11,19 L27,3" fill="none" stroke="var(--sky)" stroke-width="5" stroke-linecap="round" stroke-linejoin="round"/></svg>Lorem ipsum dolor</li>
    <li><svg viewBox="0 0 30 22"><path d="M3,11 L11,19 L27,3" fill="none" stroke="var(--sky)" stroke-width="5" stroke-linecap="round" stroke-linejoin="round"/></svg>Lorem ipsum dolor</li>
  </ul>

  <h2 class="pitch-title">Sie wollen Ihre<br>Immobilie veräußern<br>oder verwalten<br>lassen?</h2>
  <p class="pitch-text">Lorem ipsum dolor sit amet, consectetuer adipiscing elit, ed diam nonummy nibh euismod Lorem ipsum dolor sit amet, consectetuer adipiscing elit, ed diam nonummy nibh euismod Lorem ipsum dolor sit amet, consectetuer adipiscing elit, ed diam nonummy nibh euismod Lorem ipsum dolor sit amet, consectetuer adipiscing elit, ed diam nonummy nibh</p>

  <ul class="benefits">
    <li><span class="dot"></span><p>Lorem ipsum dolor sit amet, consectetuer adipiscing elit, ed diam nonummy nibh euismod</p></li>
    <li class="strong"><span class="dot"></span><p>Lorem ipsum dolor sit amet, consectetuer adipiscing elit, ed diam nonummy nibh euismod</p></li>
    <li><span class="dot"></span><p>Lorem ipsum dolor sit amet, consectetuer adipiscing elit, ed diam nonummy nibh euismod</p></li>
  </ul>

  <p class="slogan">Alles rund ums Haus für Berlin &amp; Brandenburg</p>

  <div class="contact-row">
    <span class="item"><span class="icon"><svg viewBox="0 0 16 16"><path d="M4,1 L6.5,5 L5,6.5 C6,8.5 7.5,10 9.5,11 L11,9.5 L15,12 L13,15 C7,14.5 1.5,9 1,3 Z" fill="var(--navy)"/></svg></span>030/55501234</span>
    <span class="item"><span class="icon"><svg viewBox="0 0 16 16"><rect x="1.5" y="3.5" width="13" height="9" fill="var(--navy)"/><path d="M1.5,3.5 L8,9 L14.5,3.5" fill="none" stroke="#fff" stroke-width="1.2"/></svg></span>info@valtmer-home.example</span>
    <span class="item"><span class="icon"><svg viewBox="0 0 16 16"><circle cx="8" cy="8" r="6.5" fill="none" stroke="var(--navy)" stroke-width="1.2"/><ellipse cx="8" cy="8" rx="3" ry="6.5" fill="none" stroke="var(--navy)" stroke-width="1.1"/><path d="M1.5,8 H14.5 M2.5,5 H13.5 M2.5,11 H13.5" stroke="var(--navy)" stroke-width="1"/></svg></span>www.valtmer-home.example</span>
  </div>
</main>
</body>
</html>
```